Business Card design for insurance broker in Denver, CO, USA

I need a business card designed using this logo that was just created. We sell life and disability income insurance to US consumers.
Looking for a professionally designed card to make use of the logo and have something to hand to prospects or new business referral sources. The card could be white, gray, black or whatever you would recommend.

Target Market(s)

US Consumers and other financial professionals that I partner with.

Industry/Entity Type

Insurance Broker

Contact Information for Business Card

Owen R. Tessler, CLU, LUTCF (please note that CLU should have a superscript R in a circle for registered trademark)
President
phone (303) 555-0147
email owen@brightlakecoverage.com
4620 W. Hollister Rd, Suite 310, Cedar Hollow, CO 80999
Somewhere fit in a tagline saying "Your resource for life, long term care, and disability insurance" (maybe the back if it doesn't fit on the front, your call)

Font styles to use
Sans Serif

Requirements
Must have
• Must have logo in correct blue and gray colors, my name, address, phone, email. Order and placement determined by the designer.
• I just want something that looks a more professional than what I could have done using the business card designer tool on printmakerhub.com or CardNest, or any other do-it-yourself tool
• A regular rectangular business card with square corners is preferred
Nice to have
• I included the logos of 2 organizations I belong to (GQLF and BEPWO). They should be small, but visible on the back only. If it doesn’t look good, this is not a requirement, feel free to drop it.
Should not have
• Do not add any colors not already in the logo, except use of black and whites which are okay. If you use the logo on the back and want to make that in all black, gray or white, that may be okay as well.

```html
<!DOCTYPE html>
<html lang="en">
<head>
<meta charset="utf-8">
<title>Brightlake Coverage – Business Card</title>
<link href="https://fonts.googleapis.com/css2?family=Lato:wght@300;400;700&display=swap" rel="stylesheet">
<style>
  :root {
    --page-bg: #e9eaec;
    --navy-top: #0d2748;
    --navy-bottom: #020c1c;
    --brand-blue: #2f7fd6;
    --brand-gray: #9a9a9a;
    --white: #ffffff;
    --paper-bottom: #e6e7ea;
    --mosaic-dark: rgba(30, 90, 150, 0.45);
    --mosaic-light: rgba(120, 180, 225, 0.35);
  }
  * { box-sizing: border-box; margin: 0; padding: 0; }
  html, body { width: 1200px; height: 1200px; overflow: hidden; }
  body {
    background: var(--page-bg);
    font-family: 'Lato', sans-serif;
    position: relative;
  }
  .card {
    position: absolute;
    left: 225px;
    width: 750px;
    height: 450px;
    overflow: hidden;
  }
  .card--front {
    top: 128px;
    background: linear-gradient(180deg, var(--navy-top) 0%, var(--navy-top) 40%, var(--navy-bottom) 100%);
    color: var(--white);
  }
  .card--back {
    top: 647px;
    background: linear-gradient(180deg, var(--white) 0%, var(--white) 35%, var(--paper-bottom) 100%);
    color: var(--brand-blue);
  }
  .mosaic { position: absolute; }
  .mosaic--top {
    left: 0; top: 0; width: 380px; height: 150px;
    clip-path: polygon(0 0, 100% 0, 0 100%);
  }
  .mosaic--bottom {
    right: 0; bottom: 0; width: 380px; height: 150px;
    clip-path: polygon(100% 0, 100% 100%, 0 100%);
  }
  .card--front .mosaic--top { background: linear-gradient(135deg, var(--mosaic-dark), rgba(13,39,72,0) 80%); }
  .card--front .mosaic--bottom { background: linear-gradient(315deg, var(--mosaic-dark), rgba(2,12,28,0) 80%); }
  .card--back .mosaic--top { background: linear-gradient(135deg, var(--mosaic-light), rgba(255,255,255,0) 80%); }
  .card--back .mosaic--bottom { background: linear-gradient(315deg, var(--mosaic-light), rgba(230,231,234,0) 80%); }

  .brand-ring { position: absolute; }
  .card--front .brand-ring { left: 295px; top: 86px; }
  .card--back .brand-ring { left: 140px; top: 118px; }

  .brand-name {
    position: absolute;
    text-align: center;
    font-weight: 700;
    text-transform: uppercase;
    white-space: nowrap;
  }
  .card--front .brand-name {
    left: 0; width: 100%; top: 276px;
    font-size: 27px; letter-spacing: 6px; color: var(--white);
  }
  .card--back .brand-name {
    left: 0; width: 392px; top: 252px;
    font-size: 20px; letter-spacing: 3px; color: var(--brand-blue);
  }
  .tagline {
    position: absolute;
    left: 0; width: 100%; top: 330px;
    text-align: center;
    font-size: 12.5px; letter-spacing: 2.6px; line-height: 22px;
    text-transform: uppercase; font-weight: 400;
  }
  .memberships {
    position: absolute; top: 335px; left: 107px;
    display: flex; gap: 70px; align-items: center;
  }
  .badge { width: 54px; height: 48px; }
  .badge--square { background: var(--brand-blue); opacity: 0.85; }
  .badge--triangle { width: 58px; }

  .divider {
    position: absolute; left: 377px; top: 120px; width: 1px; height: 230px;
    background: linear-gradient(180deg, rgba(0,0,0,0), rgba(0,0,0,0.12), rgba(0,0,0,0));
  }
  .contact { position: absolute; left: 403px; top: 165px; }
  .contact__name {
    font-size: 24px; font-weight: 700; white-space: nowrap; letter-spacing: -0.2px;
  }
  .contact__credentials { font-size: 17px; font-weight: 300; margin-left: 6px; }
  .contact__credentials sup { font-size: 9px; }
  .contact__title { font-size: 12.5px; font-weight: 400; margin-top: 3px; }
  .contact__list { list-style: none; margin-top: 16px; font-size: 13px; line-height: 17px; }
  .contact__list li { display: flex; align-items: flex-start; margin-bottom: 8px; }
  .contact__list svg { width: 14px; height: 14px; margin-right: 16px; margin-top: 2px; flex-shrink: 0; fill: var(--brand-blue); }
</style>
</head>
<body>

<section class="card card--front" aria-label="Card front">
  <div class="mosaic mosaic--top" role="img" aria-label="Decorative mosaic of blue squares"></div>
  <div class="mosaic mosaic--bottom" role="img" aria-label="Decorative mosaic of blue squares"></div>
  <svg class="brand-ring" width="160" height="160" viewBox="0 0 160 160" aria-hidden="true">
    <circle cx="80" cy="80" r="74" fill="none" stroke="var(--white)" stroke-width="5"/>
  </svg>
  <p class="brand-name">Brightlake Coverage</p>
  <p class="tagline">Your resource for life,<br>long term care, &amp; disability insurance</p>
</section>

<section class="card card--back" aria-label="Card back">
  <div class="mosaic mosaic--top" role="img" aria-label="Decorative mosaic of light blue squares"></div>
  <div class="mosaic mosaic--bottom" role="img" aria-label="Decorative mosaic of light blue squares"></div>
  <svg class="brand-ring" width="112" height="112" viewBox="0 0 112 112" aria-hidden="true">
    <circle cx="56" cy="56" r="51" fill="none" stroke="var(--brand-blue)" stroke-width="4"/>
  </svg>
  <p class="brand-name">Brightlake Coverage</p>

  <div class="memberships" aria-label="Professional memberships">
    <div class="badge badge--square" role="img" aria-label="GQLF membership badge"></div>
    <svg class="badge badge--triangle" viewBox="0 0 58 48" role="img" aria-label="BEPWO membership badge">
      <polygon points="29,4 54,44 4,44" fill="var(--brand-blue)"/>
    </svg>
  </div>

  <div class="divider"></div>

  <div class="contact">
    <p class="contact__name">OWEN R. TESSLER<span class="contact__credentials">CLU<sup>®</sup>, LUTCF</span></p>
    <p class="contact__title">PRESIDENT</p>
    <ul class="contact__list">
      <li>
        <svg viewBox="0 0 24 24" aria-hidden="true"><path d="M6.6 10.8a15 15 0 0 0 6.6 6.6l2.2-2.2a1 1 0 0 1 1-.25 11.4 11.4 0 0 0 3.6.57 1 1 0 0 1 1 1V20a1 1 0 0 1-1 1A17 17 0 0 1 3 4a1 1 0 0 1 1-1h3.5a1 1 0 0 1 1 1c0 1.25.2 2.45.57 3.57a1 1 0 0 1-.25 1z"/></svg>
        <span>(303) 555-0147</span>
      </li>
      <li>
        <svg viewBox="0 0 24 24" aria-hidden="true"><path d="M2 5h20v14H2z" fill="var(--brand-blue)"/><path d="M3 6l9 7 9-7" fill="none" stroke="var(--white)" stroke-width="1.6"/></svg>
        <span>owen@brightlakecoverage.com</span>
      </li>
      <li>
        <svg viewBox="0 0 24 24" aria-hidden="true"><path d="M12 2a7 7 0 0 0-7 7c0 5.2 7 13 7 13s7-7.8 7-13a7 7 0 0 0-7-7zm0 9.5A2.5 2.5 0 1 1 12 6.5a2.5 2.5 0 0 1 0 5z"/></svg>
        <span>4620 W. Hollister Rd, Suite 310,<br>Cedar Hollow, CO 80999</span>
      </li>
    </ul>
  </div>
</section>

</body>
</html>
```